Dog treat bakery needs updated bag labels

We're a small-batch dog treat bakery and would like to update our front bag labels to 1) differentiate our line of products and 2) to stand out on shelves. We believe all dogs deserve to eat clean, healthy foods. That's why we bake low-calorie, clean treats made with simple, premium ingredients like teff, amaranth, and sorghum flours and 100% blueberry, carrot, and purple sweet potato. All our treats are made gluten free without preservatives, artificial flavors, soy, corn, wheat, or eggs. Clean treats, happy dogs!

see uploaded files

```html
<!DOCTYPE html>
<html lang="en">
<head>
<meta charset="utf-8">
<title>Goofy Pup – Dog Treat Bag Labels</title>
<link href="https://fonts.googleapis.com/css2?family=Bebas+Neue&family=Libre+Baskerville:wght@400;700&display=swap" rel="stylesheet">
<style>
:root{
  --teal:#1a9da6;
  --white:#ffffff;
  --ink:#2f2f2f;
  --charcoal:#333333;
  --blueberry:#2b5ba3;
  --carrot:#f07223;
  --peanut:#c99a7b;
  --cheese:#a97ab8;
  --brown:#9a4a25;
}
*{margin:0;padding:0;box-sizing:border-box}
html,body{width:1200px;height:4342px;overflow:hidden;background:var(--white)}
.sheet{position:relative;width:1200px;height:4342px}
.label{position:absolute;left:78px;width:1046px;height:605px;background:var(--teal);overflow:hidden}
.hearts{position:absolute;left:25px;top:50px;width:275px;height:525px;border-radius:40px;
  background:radial-gradient(ellipse at 50% 45%,rgba(255,255,255,.28),rgba(255,255,255,.08) 70%,rgba(255,255,255,0))}
.panel{position:absolute;left:0;top:0;width:1046px;height:605px}
.panel path{fill:var(--panel)}
.seal{position:absolute;left:341px;top:141px;width:328px;height:328px;border-radius:50%;background:var(--white);
  display:flex;align-items:center;justify-content:center}
.seal::before{content:"";position:absolute;inset:22px;border-radius:50%;border:4px solid var(--teal)}
.brand{font-family:"Libre Baskerville",serif;font-weight:700;font-size:34px;color:var(--brown);text-align:center}
.claim{position:absolute;left:283px;width:420px;top:24px;text-align:center;font-family:"Libre Baskerville",serif;font-size:25px;color:var(--claim)}
.kind{position:absolute;left:283px;width:420px;top:60px;text-align:center;font-family:"Bebas Neue",sans-serif;font-size:60px;line-height:1;color:var(--white)}
.name{position:absolute;left:283px;width:420px;top:500px;text-align:center;font-family:"Libre Baskerville",serif;font-weight:700;font-size:35px;letter-spacing:1px;color:var(--name)}
.name small{display:block;font-size:25px;line-height:1}
.net{position:absolute;left:283px;width:420px;top:556px;text-align:center;font-family:"Libre Baskerville",serif;font-size:18px;color:var(--net)}
.facts{position:absolute;left:787px;top:62px;width:240px;font-family:"Bebas Neue",sans-serif;font-size:31px;line-height:44px;color:var(--white);letter-spacing:.5px}
.facts p{margin-bottom:44px}
.pill{position:absolute;left:743px;top:511px;height:62px;padding:0 22px;border-radius:31px;background:var(--panel);
  font-family:"Bebas Neue",sans-serif;font-size:30px;line-height:62px;color:var(--white);white-space:nowrap}
.pill.wide{left:763px;font-size:24px}
.maple{--panel:var(--charcoal);--claim:var(--teal);--name:var(--teal);--net:var(--white)}
.berry{--panel:var(--blueberry);--claim:var(--white);--name:var(--white);--net:var(--white)}
.carrot{--panel:var(--carrot);--claim:var(--ink);--name:var(--ink);--net:var(--white)}
.peanut{--panel:var(--peanut);--claim:var(--ink);--name:var(--ink);--net:var(--white)}
.cheese{--panel:var(--cheese);--claim:var(--white);--name:var(--white);--net:var(--ink)}
.peanut .name{top:478px}
.peanut .net{top:570px}
</style>
</head>
<body>
<main class="sheet">

<section class="label maple" style="top:91px">
  <div class="hearts" role="img" aria-label="White outline hearts decoration"></div>
  <svg class="panel" viewBox="0 0 1046 605"><path d="M345,0 L666,0 C690,150 703,200 703,302 C703,405 690,455 666,605 L345,605 C321,455 283,405 283,302 C283,200 321,150 345,0 Z"/></svg>
  <p class="claim">gluten free</p>
  <h2 class="kind">DOG TREATS</h2>
  <div class="seal"><span class="brand">Goofy Pup</span></div>
  <h3 class="name">Maple’s Morsels</h3>
  <p class="net">Net Wt 4 OZ (113g)</p>
  <div class="facts"><p>NO<br>SOY, CORN,<br>WHEAT, EGGS<br>OR DAIRY</p><p>MADE WITH<br>ANCIENT GRAINS<br>AND GRASS FED<br>BEEF LIVER</p></div>
  <span class="pill">10 CALORIES EACH</span>
</section>

<section class="label berry" style="top:792px">
  <div class="hearts" role="img" aria-label="White outline hearts decoration"></div>
  <svg class="panel" viewBox="0 0 1046 605"><path d="M345,0 L666,0 C690,150 703,200 703,302 C703,405 690,455 666,605 L345,605 C321,455 283,405 283,302 C283,200 321,150 345,0 Z"/></svg>
  <p class="claim">gluten free</p>
  <h2 class="kind">DOG TREATS</h2>
  <div class="seal"><span class="brand">Goofy Pup</span></div>
  <h3 class="name">Berry Burst</h3>
  <p class="net">Net Wt 4 OZ (113g)</p>
  <div class="facts"><p>NO<br>SOY, CORN,<br>WHEAT, EGGS<br>OR DAIRY</p><p>100%<br>BLUBERRY</p><p>FULL OF<br>ANTIOXIDANTS!</p></div>
  <span class="pill">ONLY 1 CALORIES EACH</span>
</section>

<section class="label carrot" style="top:1505px">
  <div class="hearts" role="img" aria-label="White outline hearts decoration"></div>
  <svg class="panel" viewBox="0 0 1046 605"><path d="M345,0 L666,0 C690,150 703,200 703,302 C703,405 690,455 666,605 L345,605 C321,455 283,405 283,302 C283,200 321,150 345,0 Z"/></svg>
  <p class="claim">gluten and grain free</p>
  <h2 class="kind">DOG TREATS</h2>
  <div class="seal"><span class="brand">Goofy Pup</span></div>
  <h3 class="name">Comet Carrot</h3>
  <p class="net">Net Wt 4 OZ (113g)</p>
  <div class="facts"><p>NO<br>SOY, CORN,<br>WHEAT, EGGS<br>OR DAIRY</p><p>MADE WITH<br>CARROT<br>AND PURPLE<br>SWEET POTATO</p></div>
  <span class="pill">1.5 CALORIES EACH</span>
</section>

<section class="label peanut" style="top:2224px">
  <div class="hearts" role="img" aria-label="White outline hearts decoration"></div>
  <svg class="panel" viewBox="0 0 1046 605"><path d="M345,0 L666,0 C690,150 703,200 703,302 C703,405 690,455 666,605 L345,605 C321,455 283,405 283,302 C283,200 321,150 345,0 Z"/></svg>
  <p class="claim">gluten and grain free</p>
  <h2 class="kind">DOG TREATS</h2>
  <div class="seal"><span class="brand">Goofy Pup</span></div>
  <h3 class="name">Peanut Butter<small>Nibble Nums</small></h3>
  <p class="net">Net Wt 4 OZ (113g)</p>
  <div class="facts"><p>NO<br>SOY, CORN, WHEAT,<br>EGGS OR DAIRY</p><p>MADE WITH<br>REAL PEANUT<br>BUTTER</p><p>FIND<br>THE LUCKY BONE!</p></div>
  <span class="pill">3 CALORIES EACH</span>
</section>

<section class="label peanut" style="top:2937px">
  <div class="hearts" role="img" aria-label="White outline hearts decoration"></div>
  <svg class="panel" viewBox="0 0 1046 605"><path d="M345,0 L666,0 C690,150 703,200 703,302 C703,405 690,455 666,605 L345,605 C321,455 283,405 283,302 C283,200 321,150 345,0 Z"/></svg>
  <p class="claim">gluten and grain free</p>
  <h2 class="kind">DOG TREATS</h2>
  <div class="seal"><span class="brand">Goofy Pup</span></div>
  <h3 class="name">Peanut Butter<small>Nibble Nums</small></h3>
  <p class="net">Net Wt 4 OZ (113g)</p>
  <div class="facts"><p>NO<br>SOY, CORN, WHEAT,<br>EGGS OR DAIRY</p><p>MADE WITH<br>REAL PEANUT<br>BUTTER</p><p>FIND<br>THE LUCKY BONE !</p></div>
  <span class="pill wide">LESS THAN 1 CALORIES EACH</span>
</section>

<section class="label cheese" style="top:3648px">
  <div class="hearts" role="img" aria-label="White outline hearts decoration"></div>
  <svg class="panel" viewBox="0 0 1046 605"><path d="M345,0 L666,0 C690,150 703,200 703,302 C703,405 690,455 666,605 L345,605 C321,455 283,405 283,302 C283,200 321,150 345,0 Z"/></svg>
  <p class="claim">gluten and grain free</p>
  <h2 class="kind">DOG TREATS</h2>
  <div class="seal"><span class="brand">Goofy Pup</span></div>
  <h3 class="name">Rosie’s Snacks</h3>
  <p class="net">Net Wt 4 OZ (113g)</p>
  <div class="facts" style="top:110px"><p>NO<br>SOY, CORN,<br>WHEAT, EGGS<br>OR DAIRY</p><p>MADE WITH<br>VEGAN CHEESE</p></div>
  <span class="pill">ONLY 1.5 CALORIES EACH</span>
</section>

</main>
</body>
</html>
```